KRM

I just wrote a novel that I plan on marketing through my website. Please use my uploaded files to add on to your design... The name of the book is "Lanterns under the frost".

Industry/Entity Type

Marketing

Font styles to use
Serif
Sans Serif

Colors

Designer to choose colors to be used in the design.

```html
<!DOCTYPE html>
<html lang="en">
<head>
<meta charset="utf-8">
<title>KRM — Lanterns under the frost</title>
<link rel="stylesheet" href="https://fonts.googleapis.com/css2?family=Carlito:wght@400;700&family=Open+Sans:wght@400;600&family=Arimo:wght@400&display=swap">
<style>
  :root {
    --white: #ffffff;
    --ink: #1a1a1a;
    --text: #3a3a3a;
    --nav: #444444;
    --red: #d4151c;
    --red-dark: #b10f15;
    --navy: #2b2766;
    --wood-dark: #252323;
    --wood-mid: #2f2d2c;
    --shelf-light: #f0cf9c;
    --shelf-dark: #c9975c;
    --footer: #000000;
    --footer-text: #c8c8c8;
    --field-border: #cfcfcf;
  }
  * { box-sizing: border-box; margin: 0; padding: 0; }
  html, body { width: 1200px; height: 874px; overflow: hidden; }
  body { position: relative; background: var(--wood-dark); font-family: "Open Sans", Arial, sans-serif; color: var(--text); }

  .site-header { position: absolute; left: 0; top: 0; width: 1200px; height: 147px; background: var(--white); }
  .brand { position: absolute; left: 109px; top: 40px; display: flex; align-items: center; gap: 14px; }
  .brand-dot { width: 64px; height: 64px; border-radius: 50%; background: var(--ink); }
  .brand-name { font-family: "Carlito", Arial, sans-serif; font-weight: 700; font-size: 44px; color: var(--ink); letter-spacing: 1px; }

  .social { position: absolute; display: flex; gap: 8px; }
  .social-header { right: 110px; top: 27px; }
  .social-footer { right: 110px; top: 818px; }
  .social a { display: block; width: 34px; height: 34px; border-radius: 50%; }
  .social-header a { background: var(--navy); }
  .social-footer a { background: var(--white); }

  .contact-line { position: absolute; right: 110px; top: 78px; font-family: "Open Sans", Arial, sans-serif; font-weight: 600; font-size: 15.5px; color: var(--nav); }
  .contact-line .phone { color: var(--red); }

  .main-nav { position: absolute; right: 110px; top: 113px; display: flex; font-size: 15px; }
  .main-nav a { color: var(--nav); text-decoration: none; padding: 0 9px; border-left: 1px solid #cfcfcf; line-height: 16px; }
  .main-nav a:first-child { border-left: none; }
  .main-nav a:last-child { padding-right: 0; }

  .hero { position: absolute; left: 0; top: 147px; width: 1200px; height: 649px;
    background: linear-gradient(90deg, var(--wood-dark), var(--wood-mid) 30%, var(--wood-dark) 60%, var(--wood-mid) 85%, var(--wood-dark)); }
  .hero-copy { position: absolute; left: 182px; top: 82px; width: 320px; color: var(--white); }
  .hero-title { font-family: "Carlito", Arial, sans-serif; font-weight: 700; font-size: 26px; line-height: 34px; }
  .hero-text { margin-top: 8px; font-family: "Arimo", Arial, sans-serif; font-size: 12.5px; line-height: 22px; }
  .buy-button { position: absolute; left: 182px; top: 254px; width: 197px; height: 50px; border: 2px solid var(--white); border-radius: 5px;
    background: linear-gradient(var(--red), var(--red-dark)); color: var(--white); font-family: "Carlito", Arial, sans-serif; font-weight: 700; font-size: 21px;
    display: flex; align-items: center; justify-content: center; text-decoration: none; }

  .slider-arrow { position: absolute; top: 200px; width: 37px; height: 37px; }
  .slider-arrow.prev { left: 109px; }
  .slider-arrow.next { left: 1053px; }

  .book-back { position: absolute; left: 527px; top: 128px; width: 210px; height: 240px; border: 5px solid var(--white);
    background: linear-gradient(160deg, #3a3588, #2c286a 60%, #4a2d5a); transform: rotate(-15deg); box-shadow: 0 4px 10px rgba(0,0,0,.5); }
  .book-front { position: absolute; left: 764px; top: 33px; width: 260px; height: 337px; border: 5px solid var(--white);
    background: linear-gradient(170deg, #ece6e0, #b8463c 30%, #8a6a5a 60%, #4a3e3a); box-shadow: 0 4px 12px rgba(0,0,0,.5); }
  .shelf { position: absolute; left: 120px; top: 364px; width: 960px; height: 25px;
    background: linear-gradient(var(--shelf-light), var(--shelf-dark)); clip-path: polygon(2% 0, 98% 0, 100% 70%, 100% 100%, 0 100%, 0 70%); }

  .card { position: absolute; top: 410px; width: 486px; height: 218px; background: var(--white); border-radius: 4px; padding: 16px 24px 0; }
  .card-about { left: 109px; }
  .card-newsletter { left: 612px; width: 476px; }
  .card-title { font-family: "Carlito", Arial, sans-serif; font-weight: 700; font-size: 23px; color: var(--ink); line-height: 30px; }
  .card-text { font-size: 13px; line-height: 21px; color: var(--text); margin-top: 3px; }
  .card-icon { position: absolute; top: 12px; right: 24px; }
  .card-mark { font-family: "Carlito", Arial, sans-serif; font-weight: 700; font-size: 38px; color: var(--red); line-height: 38px; }
  .learn-more { position: absolute; left: 25px; top: 181px; width: 104px; height: 26px; border-radius: 3px; background: var(--navy); color: var(--white);
    font-family: "Carlito", Arial, sans-serif; font-size: 15px; display: flex; align-items: center; justify-content: center; text-decoration: none; }

  .field { position: absolute; left: 24px; width: 255px; height: 29px; border: 1px solid var(--field-border); border-radius: 3px;
    font-size: 11px; color: var(--text); padding-left: 12px; display: flex; align-items: center; box-shadow: inset 0 1px 2px rgba(0,0,0,.08); }
  .field-name { top: 105px; }
  .field-email { top: 147px; }
  .go-button { position: absolute; left: 293px; top: 112px; width: 53px; height: 55px; border-radius: 50%; background: var(--navy);
    box-shadow: 0 3px 0 #1a1745; color: var(--white); font-family: "Carlito", Arial, sans-serif; font-weight: 700; font-size: 21px;
    display: flex; align-items: center; justify-content: center; }

  .site-footer { position: absolute; left: 0; top: 796px; width: 1200px; height: 78px; background: var(--footer); }
  .footer-nav { position: absolute; left: 109px; top: 18px; display: flex; gap: 16px; font-size: 12.5px; }
  .footer-nav a { color: var(--footer-text); text-decoration: none; }
  .copyright { position: absolute; left: 109px; top: 41px; font-size: 11.5px; color: var(--footer-text); }
</style>
</head>
<body>
  <header class="site-header">
    <div class="brand"><span class="brand-dot"></span><span class="brand-name">KRM</span></div>
    <nav class="social social-header" aria-label="Social links">
      <a href="#" aria-label="Social network one"></a>
      <a href="#" aria-label="Social network two"></a>
      <a href="#" aria-label="Social network three"></a>
    </nav>
    <p class="contact-line">CONTACT DANA HOLT : <span class="phone">555-014-2290</span></p>
    <nav class="main-nav">
      <a href="#">Home</a><a href="#">About Us</a><a href="#">News</a><a href="#">Contact Us</a>
    </nav>
  </header>

  <section class="hero">
    <div class="hero-copy">
      <h1 class="hero-title">LANTERNS UNDER<br>THE FROST</h1>
      <p class="hero-text">Lorem Ipsum is simply dummy text of the printing and typesetting industry. Lorem Ipsum has been the industry's standard dummy<br>text ever since the 1500s,</p>
    </div>
    <a href="#" class="buy-button">Buy Now - $14.99</a>

    <svg class="slider-arrow prev" viewBox="0 0 37 37" aria-label="Previous slide">
      <circle cx="18.5" cy="18.5" r="16.5" fill="none" stroke="#fff" stroke-width="3"/>
      <path d="M21 11 L14 18.5 L21 26" fill="none" stroke="#fff" stroke-width="3.5" stroke-linecap="round" stroke-linejoin="round"/>
    </svg>
    <svg class="slider-arrow next" viewBox="0 0 37 37" aria-label="Next slide">
      <circle cx="18.5" cy="18.5" r="16.5" fill="none" stroke="#fff" stroke-width="3"/>
      <path d="M16 11 L23 18.5 L16 26" fill="none" stroke="#fff" stroke-width="3.5" stroke-linecap="round" stroke-linejoin="round"/>
    </svg>

    <div class="book-back" role="img" aria-label="Back cover of the novel Lanterns under the frost"></div>
    <div class="book-front" role="img" aria-label="Promotional poster for the novel Lanterns under the frost"></div>
    <div class="shelf"></div>

    <article class="card card-about">
      <h2 class="card-title">About Lanterns</h2>
      <span class="card-icon card-mark">?</span>
      <p class="card-text">Lorem Ipsum is simply dummy text of the printing and typesetting industry. Lorem Ipsum has been the industry's standard dummy text ever since the 1500s, when an unknown printer took a galley of type and scrambled it to make a type specimen book. It has survived not only five centuries, but also the leap into electronic typesetting, remaining essentially unchanged.</p>
      <a href="#" class="learn-more">Learn More</a>
    </article>

    <article class="card card-newsletter">
      <h2 class="card-title">Newsletter</h2>
      <svg class="card-icon" width="28" height="26" viewBox="0 0 28 26" aria-label="Mail">
        <path d="M2 11 L14 2 L26 11 L26 24 L2 24 Z" fill="var(--red)"/>
        <path d="M5 11 L14 18 L23 11" fill="none" stroke="#fff" stroke-width="2"/>
        <path d="M3 23 L11 16 M25 23 L17 16" stroke="#fff" stroke-width="2"/>
      </svg>
      <p class="card-text">Keep up to date with new book releases and announcements<br>with our newsletter.</p>
      <div class="field field-name">Name</div>
      <div class="field field-email">Email Address</div>
      <div class="go-button">GO</div>
    </article>
  </section>

  <footer class="site-footer">
    <nav class="footer-nav"><a href="#">Home</a><a href="#">About Us</a><a href="#">News</a><a href="#">Contact Us</a></nav>
    <p class="copyright">Copyright © 2014 Lanterns under the frost.&nbsp; All Rights Reserved</p>
  </footer>
  <nav class="social social-footer" aria-label="Social links">
    <a href="#" aria-label="Social network one"></a>
    <a href="#" aria-label="Social network two"></a>
    <a href="#" aria-label="Social network three"></a>
  </nav>
</body>
</html>
```